Corvane Works Inc. The PPT to sell our ideas, what we believe in and our products.

We are looking to have our PPT updated, to be more dynamic and engaging. We are a new Technology company that specializes in Software as a Service (SaaS). By utilizing mature open source software and various online technical communities, we provide companies and government agencies with the best of breed open source software, open innovation, and crowdsourcing for software/system development. We are able to deliver the highest quality, peer vetted software solutions more quickly and for much less capital investment than traditional Software development companies.
This Presentation will be shown to potential customs. We are going to have to introduce them to what we do, (utilize open source technologies, crowdsourcing, open innovation to build software) why it is better than the traditional way of developing software,(using the same in-house IT folks that they have for ever) and then make them want to use our company to jumpstart their IT development. By hiring us to build an Tidal SaaS software solution to their IT pain point.

The final design should communicate that we strongly believe in open innovation, crowdsourcing, open source technology/software, and how these areas are going to change the way companies and government procure their software.
That our product is the future and the only way that Governments and companies are going to be able to keep pace with new technologies, stay current and relevant, and to also better serve their customers. We are helping companies to realize new solutions to the problems that the have in their current businesses.
We would like to use 2 blues for sure in the PPT, (#BDCEE9, #293178), please feel free to use other colors as well. We just do not want to have the look or feel of the American Flag. So if you use Red, please be conscious of that.

We are looking for something that has a bold dynamic look and feel to it. We need something that screams open innovation, crowdsourcing, open source technology, and changing the way GOVT buys software. We want eye grabbing, interesting designs that can be translated into a great company endorsement.

Project Deadline Extended Reason: I am extending the deadline for the contest by five days, due to the fact that I just started to receive some better designs. I wanted to allow time for the designers that have submitted already to incorporate a few modifications to their designs to be a little more in-line with what our company is looking for out of this contest.Please see the updated brief for additional information. Thank you again for the time and effort everyone is putting into this contest!! Added Sunday, May 31, 2015

Target Market(s)

government / state agencies (conservative folks that do not really like change), larger companies that can spend a few million dollars on an IT software solution.

Industry/Entity Type

It Company

Font styles to use
Serif
Sans Serif

Colors
86cae7
86cfc6
abd037
9bcb3c
fbee3d
faa54b
f37122
f04a50
b868aa

Requirements
Must have
• the logo, the 2 blues from the description.
• We would like to have a various colors and a lot of life in the presentation.
• incorporate or three logos, so that we can see which one works the best for each design...i do not want a 3 designs on the same slide at the same time, i want to see the same slide 3 times with one logo on it at a time.
Nice to have
• some animations, to get the customers interested and engaged, during the beginning of the slide deck where we are explaining what crowdsourcing and open source software is.
Should not have
• Do not want it to feel or look like the american flag. We want it to be bold, but the red, white, blue combo scares us a little.
• We are an open innovation company and we need our PPT to SCREAM the fact that we are not your average software development company.....That we are an exciting, fresh, innovative company and are going to change the way that governments get the software technology

```html
<!DOCTYPE html>
<html lang="en">
<head>
<meta charset="utf-8">
<title>Corvane Works – Crowdsourcing</title>
<link href="https://fonts.googleapis.com/css2?family=Open+Sans:wght@400;600;700&display=swap" rel="stylesheet">
<style>
  :root {
    --navy: #293178;
    --sky: #bdcee9;
    --orange: #f37122;
    --purple: #b868aa;
    --teal: #86cfc6;
    --lime: #9bcb3c;
    --ink: #555a60;
    --ink-soft: #6d7176;
    --band: #efefef;
    --cell-a: #eeeeee;
    --cell-b: #dcdcdc;
    --white: #ffffff;
  }
  * { box-sizing: border-box; margin: 0; padding: 0; }
  html, body { width: 798px; height: 1200px; overflow: hidden; background: var(--white); }
  body { font-family: "Open Sans", Arial, sans-serif; color: var(--ink); position: relative; }

  .slide { position: absolute; left: 0; width: 798px; background: var(--white); overflow: hidden; }
  .slide--intro { top: 0; height: 596px; }
  .slide--types { top: 604px; height: 596px; }

  .slide__header { position: absolute; left: 0; top: 0; width: 100%; height: 90px; border-bottom: 4px solid var(--navy); }
  .slide__title { position: absolute; left: 22px; top: 28px; font-size: 24px; font-weight: 400; color: var(--navy); }

  .brand { position: absolute; right: 14px; top: 14px; width: 114px; height: 62px; text-align: center; }
  .brand__mark { display: block; width: 16px; height: 16px; background: var(--navy); margin: 2px auto 6px; }
  .brand__name { display: block; font-size: 14px; font-weight: 700; color: var(--navy); line-height: 16px; letter-spacing: 0.5px; }

  .lede { position: absolute; left: 0; top: 96px; width: 100%; height: 72px; background: var(--band);
          text-align: center; font-size: 19px; line-height: 25px; color: var(--ink-soft); padding-top: 11px; }

  .model { position: absolute; top: 184px; width: 246px; height: 348px; background: var(--white);
           border: 1px solid #e2e2e2; border-top: 5px solid var(--teal);
           box-shadow: 0 2px 6px rgba(0,0,0,0.18); padding: 10px 10px; }
  .model--traditional { left: 14px; border-top-color: var(--orange); }
  .model--crowd { left: 276px; border-top-color: var(--lime); }
  .model--user { left: 539px; border-top-color: var(--purple); }
  .model__name { font-size: 18px; font-weight: 700; color: var(--navy); margin-bottom: 12px; }
  .model p { font-size: 16px; line-height: 23px; color: var(--ink-soft); margin-bottom: 22px; }
  .model__label { font-weight: 700; color: var(--ink-soft); font-size: 16px; }
  .model ul { list-style: none; font-size: 16px; line-height: 23px; color: var(--ink-soft); }

  .slide__footer { position: absolute; left: 0; bottom: 0; width: 100%; height: 50px; background: var(--navy);
                   color: var(--white); font-size: 10.5px; font-weight: 700; padding: 18px 0 0 20px; z-index: 2; }

  .types { position: absolute; left: 9px; top: 96px; width: 780px; table-layout: fixed;
           border-collapse: separate; border-spacing: 5px; }
  .types th { height: 53px; color: var(--white); font-size: 16px; font-weight: 700; line-height: 20px; text-align: center; }
  .types th.c1 { background: var(--orange); }
  .types th.c2 { background: var(--navy); }
  .types th.c3 { background: var(--purple); }
  .types th.c4 { background: var(--navy); }
  .types td { font-size: 10.5px; line-height: 13px; color: var(--ink-soft); padding: 4px 9px; vertical-align: middle; height: 88px; }
  .types td.a { background: var(--cell-a); } .types td.b { background: var(--cell-b); }
  .types td.kind { font-weight: 700; font-size: 11.5px; line-height: 15px; }
  .types ul { padding-left: 13px; }
</style>
</head>
<body>

<section class="slide slide--intro">
  <header class="slide__header">
    <h1 class="slide__title">What the Crowdsourcing?</h1>
    <div class="brand"><span class="brand__mark"></span><span class="brand__name">CORVANE<br>WORKS</span></div>
  </header>
  <div class="lede">Crowdsourcing is a blend of traditional top-down<br>production and bottom-up user production.</div>

  <article class="model model--traditional">
    <h2 class="model__name">Traditional production</h2>
    <p>Top-down, hierarchical process</p>
    <p>Locus of control in the organization</p>
    <div class="model__label">Examples:</div>
    <ul><li>In-house product development</li><li>Simple voting, marketing campaigns</li></ul>
  </article>
  <article class="model model--crowd">
    <h2 class="model__name">Crowdsourcing</h2>
    <p>Shared top-down and bottom-up process</p>
    <p>Locus of control in between organization and online community</p>
    <div class="model__label">Examples:</div>
    <ul><li>Peer Claim Review</li><li>Brightquest</li><li>Taskfield Microwork</li></ul>
  </article>
  <article class="model model--user">
    <h2 class="model__name">User produciton</h2>
    <p>Bottom-up, grassroots process</p>
    <p>Locus of control in the online community</p>
    <div class="model__label">Examples:</div>
    <ul><li>Open source software</li><li>Lorewiki</li><li>ClipHarbor</li></ul>
  </article>

  <footer class="slide__footer">Replicated from: “Using Crowdsourcing in Government.” Halvern Center for Public Operations. Marlo T. Quennell, Elmridge University. 2013.</footer>
</section>

<section class="slide slide--types">
  <header class="slide__header">
    <h1 class="slide__title">Four types of problems are suited to crowdsourcing</h1>
    <div class="brand"><span class="brand__mark"></span><span class="brand__name">CORVANE<br>WORKS</span></div>
  </header>

  <table class="types">
    <thead>
      <tr><th class="c1">Type of<br>crowdsourcing</th><th class="c2">How it<br>works</th><th class="c3">Types of<br>problems</th><th class="c4">Use case<br>for governments</th></tr>
    </thead>
    <tbody>
      <tr>
        <td class="kind a">Knowledge Discovery &amp; Management</td>
        <td class="b">Organization tasks crowd with finding and collecting information in a common location and format</td>
        <td class="a"><ul><li>Information gathering</li><li>Organization</li><li>Reporting problems</li><li>Creation of collective resources</li></ul></td>
        <td class="b"><ul><li>Reporting conditions of parks, hiking trails, roads</li><li>Tracking use of public transit</li><li>Cataloging public art projects &amp; murals for historical boards</li></ul></td>
      </tr>
      <tr>
        <td class="kind b">Distributed Human Intelligence Tasking</td>
        <td class="a">Organization tasks crowd with organizing large volumes of information</td>
        <td class="b">Distributed Human Intelligence Tasking</td>
        <td class="a"><ul><li>Language translation</li><li>Data entry</li><li>Behavioral modeling</li></ul></td>
      </tr>
      <tr>
        <td class="kind a">Broadcast Search</td>
        <td class="b">Organization tasks crowd with solving empirical problems</td>
        <td class="a">Ideation for problems with empirically provable solutions, such as scientific problems</td>
        <td class="b"><ul><li>Better algorithms for timing, traffic signals</li><li>Improving actuarial solutions</li></ul></td>
      </tr>
      <tr>
        <td class="kind b">Peer-Vetted Creative Production</td>
        <td class="a">Organization tasks crowd with creating and / or selecting creative ideas</td>
        <td class="b"><ul><li>Ideation on matters of taste</li><li>Testing market support</li><li>Design or aesthetic solutions</li></ul></td>
        <td class="a"><ul><li>Designs for public art projects</li><li>Urban or transit plans</li><li>School redistricting</li><li>Policy proposals</li></ul></td>
      </tr>
    </tbody>
  </table>

  <footer class="slide__footer">Replicated from: “Using Crowdsourcing in Government.” Halvern Center for Public Operations. Marlo T. Quennell, Elmridge University. 2013.</footer>
</section>

</body>
</html>
```